CBD oil label, sleek, clean, serious

I need graphic design for a CBD oil company. Black and white labels for 30ml amber color dropper bottles. looking for something that stands out in its simplicity. this product will be a top of the line, highest margin due to quality of ingredients. It should look rich. other products on the shelf use a lot of color and logos. this label should be clear and stand out as a place to rest your eyes in a sea of marketing glitz.

please see the idea board.

Target Market(s)

middle to older adults

Industry/Entity Type

Health And Wellness

Font styles to use
Serif

Colors
fff5ef
cadf82

Requirements
Must have
• We want the look of elegance and like an apothecary label
• Product name will be VellaSharp or VellaSoothe
• see other details on the attached idea board
Nice to have
• think Morvay and old style apothecary with a modern aesthetic
Should not have
• any reference or drawing of cannabis

```html
<!DOCTYPE html>
<html lang="en">
<head>
<meta charset="utf-8">
<title>Orla Remedy – VellaSharp Label</title>
<link href="https://fonts.googleapis.com/css2?family=Cinzel:wght@700&family=Montserrat:wght@400;500&display=swap" rel="stylesheet">
<style>
  :root {
    --ink: #1c1c1c;
    --band: #262626;
    --paper: #ffffff;
    --stage: #f1f1f1;
    --rule: #3a3a3a;
    --muted: #555555;
    --emblem-light: #f4f4f4;
    --emblem-dark: #d9d9d9;
  }
  html, body {
    margin: 0;
    width: 1200px;
    height: 1200px;
    overflow: hidden;
    background: radial-gradient(circle at 50% 45%, #fafafa 0%, var(--stage) 70%);
  }
  .label {
    position: absolute;
    left: 280px;
    top: 150px;
    width: 640px;
    height: 900px;
    background: var(--paper);
    box-shadow: 0 2px 10px rgba(0,0,0,0.08);
  }
  .label-art {
    position: absolute;
    inset: 0;
  }
  .brand-name {
    position: absolute;
    left: 0;
    right: 0;
    text-align: center;
    font-family: "Cinzel", serif;
    font-weight: 700;
    color: var(--paper);
    line-height: 1;
    margin: 0;
  }
  .brand-name .primary { display: block; font-size: 104px; letter-spacing: 4px; }
  .brand-name .secondary { display: block; font-size: 44px; letter-spacing: 6px; margin-top: 6px; }
  .brand-name { top: 360px; }
  .product-name {
    position: absolute;
    left: 0; right: 0;
    top: 572px;
    text-align: center;
    font-family: "Montserrat", sans-serif;
    font-weight: 500;
    font-size: 36px;
    color: var(--paper);
    margin: 0;
  }
  .product-type {
    position: absolute;
    left: 0; right: 0;
    top: 616px;
    text-align: center;
    font-family: "Montserrat", sans-serif;
    font-weight: 500;
    font-size: 17px;
    color: var(--paper);
    margin: 0;
  }
  .footer-line {
    position: absolute;
    top: 795px;
    left: 82px;
    right: 82px;
    display: flex;
    justify-content: space-between;
    font-family: "Montserrat", sans-serif;
    font-weight: 400;
    font-size: 23px;
    color: var(--muted);
  }
</style>
</head>
<body>
  <main class="label">
    <svg class="label-art" width="640" height="900" viewBox="0 0 640 900">
      <defs>
        <radialGradient id="emblem-fill" cx="50%" cy="50%" r="50%">
          <stop offset="0%" stop-color="var(--emblem-light)"/>
          <stop offset="100%" stop-color="var(--emblem-dark)"/>
        </radialGradient>
      </defs>
      <!-- frame -->
      <rect x="22" y="22" width="596" height="856" fill="none" stroke="var(--rule)" stroke-width="3"/>
      <rect x="38" y="38" width="564" height="824" fill="none" stroke="var(--rule)" stroke-width="1.2"/>
      <!-- emblem -->
      <g role="img" aria-label="Round sunburst emblem behind the brand name">
        <circle cx="320" cy="428" r="270" fill="none" stroke="var(--rule)" stroke-width="2"/>
        <circle cx="320" cy="428" r="252" fill="url(#emblem-fill)" stroke="var(--rule)" stroke-width="1"/>
        <circle cx="320" cy="428" r="205" fill="none" stroke="var(--rule)" stroke-width="1.5"/>
      </g>
      <!-- brand band -->
      <polygon class="brand-band"
        points="90,265 550,265 570,285 570,645 550,665 90,665 70,645 70,285"
        fill="var(--band)"/>
      <polygon points="100,280 540,280 555,295 555,635 540,650 100,650 85,635 85,295"
        fill="none" stroke="var(--paper)" stroke-width="1.5"/>
    </svg>

    <h1 class="brand-name">
      <span class="primary">ORLA</span>
      <span class="secondary">REMEDY</span>
    </h1>
    <p class="product-name">VellaSharp</p>
    <p class="product-type">Full Spectrum CBD Oil</p>

    <div class="footer-line">
      <span class="flavor">MINT FLAVOR</span>
      <span class="volume">30ml</span>
    </div>
  </main>
</body>
</html>
```